NEW Website DESIGN for Glass & Solid Surfaces Company

Brand New website, contemporary, clean, visual (images), not busy. ATTACHED IS OUR LOG THAT YOU MUST USE.

The company is called Brightwell Panes & Stoneworks (BrightwellPS)
www.brightwellps.com
The website should be www.brightwellpns.com
one page for glass one page for solid surfaces www.brightwellpanesplashes.co.uk
www.brightwellstoneworkss.co.uk

Target Market(s)

Hotels, Commercial projects, Small focus on residential

Industry/Entity Type

Construction

Number of Pages Required

5+ page

Font styles to use
Sans Serif

Requirements
Must have
• COLOURS AS PER OUR LOGO - WHITE/YELLOW/GREY - WHITE BACK GROUND
• CLEAR SIMPLE NAVIGATION - MODER CLEAN CUT - DESIGN FEEL
• LATEST NAVIGATION FOR IMAGES and text to include per project details
• WORK/PROJECT AREA - NEWS AREA - TEAM AREA/ABOUT US/CONTACT US
• NEW PAGEwww.brightwellpanesplashes.co.uk - NEW PAGE www.brightwellstoneworkss.co.uk
• PLEASE COPY THIS TYPE OF TEMPALTE
• https://www.harlowmead.co.uk/project/grand-halls/
• MOBILE READY
• WORDPRESS
• MODERN IMAGES INCLUDING VELMARA KESTRIN AND GLASS PROJECTS
Nice to have
• NEW DESIGN MODER FRESH
• WEBSITES I LIKE THE TEMPLATE SHOULD BE LIKE THE WEBSITE BELOW
• https://www.harlowmead.co.uk/
Should not have
• NOT Old fashion template, not busy NAVIGATION
• NO BLACK
• NO DARK GREYS
• NOT LOTS OF YELLOW
• RESDENTIAL IMAGES

```html
<!DOCTYPE html>
<html lang="en">
<head>
<meta charset="utf-8">
<title>Brightwell Panes &amp; Stoneworks</title>
<link href="https://fonts.googleapis.com/css2?family=Open+Sans:wght@300;400;600&display=swap" rel="stylesheet">
<style>
  :root {
    --white: #ffffff;
    --ink: #4a4d52;
    --muted: #8d9096;
    --line: #e6e7e9;
    --brand: #c9c94a;
    --wall-blue: #3f6f8c;
    --wall-warm: #cfc6b8;
    --wood: #b98a55;
  }
  * { margin: 0; padding: 0; box-sizing: border-box; }
  html, body { width: 742px; height: 1200px; overflow: hidden; background: var(--white); }
  body { font-family: "Open Sans", Arial, sans-serif; color: var(--ink); position: relative; }

  .sidebar { position: absolute; left: 0; top: 0; width: 55px; height: 1200px; background: var(--white); }
  .brand-mark { position: absolute; left: 12px; top: 10px; width: 32px; height: 32px; border-radius: 50%; background: var(--brand); }
  .brand-name { position: absolute; left: 28px; top: 56px; transform-origin: 0 0; transform: rotate(90deg) translateY(-50%);
    font-size: 8px; letter-spacing: .5px; white-space: nowrap; color: var(--muted); }
  .social { position: absolute; left: 24px; top: 322px; list-style: none; }
  .social li { width: 7px; height: 7px; border-radius: 50%; background: var(--ink); margin-bottom: 14px; }

  .hero { position: absolute; left: 55px; top: 0; width: 687px; height: 470px;
    background: linear-gradient(100deg, var(--wall-warm) 0%, #b9b2a6 30%, var(--wall-blue) 55%, #52809b 80%, #e8e4dc 100%); }
  .hero-title { position: absolute; left: 22px; top: 240px; color: var(--white); font-weight: 400; font-size: 31px; line-height: 1.18; }
  .hero-sub { position: absolute; left: 22px; top: 326px; color: var(--white); font-weight: 300; font-size: 17px; line-height: 1.25; width: 300px; }

  .intro { position: absolute; left: 80px; top: 495px; width: 620px; }
  .intro h2 { position: absolute; left: 0; top: 12px; font-weight: 400; font-size: 19px; color: var(--ink); }
  .intro p { position: absolute; top: 0; width: 148px; font-size: 7.5px; line-height: 1.55; color: var(--muted); }
  .intro .col-a { left: 205px; }
  .intro .col-b { left: 425px; }

  .gallery { position: absolute; left: 55px; top: 687px; width: 687px; height: 457px;
    display: grid; grid-template-columns: repeat(3, 1fr); grid-template-rows: repeat(2, 1fr); gap: 2px; }
  .tile { position: relative; overflow: hidden; }
  .tile .caption { position: absolute; left: 0; right: 0; bottom: 0; height: 20px; background: rgba(255,255,255,.78);
    font-size: 7.5px; line-height: 20px; padding-left: 8px; color: var(--ink); }
  .t1 { background: linear-gradient(160deg, #dfe3e4, #9fa7aa 60%, #6f7a7e); }
  .t2 { background: linear-gradient(180deg, var(--wood), #8b6438 60%, #d8cfc0); }
  .t3 { background: linear-gradient(150deg, #eef0f0, #c8cccd 55%, #7d8a90); }
  .t4 { background: linear-gradient(170deg, #4f7d98, #9ab0bd 50%, #e9e6e0); }
  .t5 { background: linear-gradient(170deg, #c9c2b4, #5a6f8c 55%, #e2ddd3); }
  .t6 { background: linear-gradient(180deg, #c49a62, #e0d7ca 45%, #30384a); }

  .footer { position: absolute; left: 75px; top: 1162px; width: 640px; font-size: 7px; color: var(--muted); }
  .footer .legal { position: absolute; right: 0; top: 0; }
  .footer .legal span { margin-left: 12px; }
</style>
</head>
<body>
  <aside class="sidebar">
    <div class="brand-mark"></div>
    <div class="brand-name">Brightwell Panes &amp; Stoneworks</div>
    <ul class="social"><li></li><li></li><li></li><li></li></ul>
  </aside>

  <header class="hero" role="img" aria-label="Hotel bedroom with blue feature wall, double bed, wooden headboard and desk chair">
    <h1 class="hero-title">Brightwell Panes<br>&amp; Stoneworks</h1>
    <p class="hero-sub">Ideal surfaces solutions for today's healthcare environment</p>
  </header>

  <section class="intro">
    <h2>Innovative designs</h2>
    <p class="col-a">With innovative designs and an enduring cool palette, Velmara® will make all of your design aspirations come true. Achieve your dreams while still attending a quality product that will stand up to whatever your life may throw at it. You can rest easy knowing you've picked a surface to last a lifetime</p>
    <p class="col-b">Achieve your dreams while still attending a quality product that will stand up to whatever your life may throw at it. You can rest easy knowing you've picked a surface to last a lifetime</p>
  </section>

  <section class="gallery">
    <div class="tile t1" role="img" aria-label="Hotel suite with sofa and window"><div class="caption">Restwell Super Suite</div></div>
    <div class="tile t2" role="img" aria-label="Wooden wall panel with sockets and desk"><div class="caption">Restwell</div></div>
    <div class="tile t3" role="img" aria-label="Bright hotel suite with bed"><div class="caption">Restwell Super Lotu Suite</div></div>
    <div class="tile t4" role="img" aria-label="Hotel room with bed and blue wall"><div class="caption">Restwell Super Room 3</div></div>
    <div class="tile t5" role="img" aria-label="Hotel room with bed and artwork"><div class="caption">Restwell Super Room 2</div></div>
    <div class="tile t6" role="img" aria-label="Wooden desk with navy chair"><div class="caption">Restwell Desk</div></div>
  </section>

  <footer class="footer">
    <span>Copyright © 2015 Brightwell Panes &amp; Stoneworks</span>
    <span class="legal"><span>Privacy Policy</span><span>Terms and Conditions</span></span>
  </footer>
</body>
</html>
```